Vetrune
@PEmmo, #128 looks good. Could I see some designs for other stationeries? Thanks
@Lumetra - #130 looks good thanks. I think we need phone number on the letterhead.
Thank you all for the inputs - these are great designs.
@Quorby, for #127, I dont think we need phone and email on the envelope. We can leave the web address. thanks.
@Lumetra - i like the idea of #96. But i dont like the black back. I like an orange back as shown #87. Also, the contact info should probably be left aligned with the logo on top.
Thanks for the inputs. I am not a fan of the color black.
@Dorvel, Could you please make the logo bigger in #91?
Dear Ju,
Pls see private message from the top right of the page..
Thanks..
Thanks for the inputs Quorby. I like #64. Would we see a variety in the font color?
Please, please - do not post pre-made templates or templates that were used in a previous contest. It does nothing but kill your credibility.

```html
<!DOCTYPE html>
<html lang="en">
<head>
<meta charset="utf-8">
<title>Vetrune Business Card</title>
<link rel="stylesheet" href="https://fonts.googleapis.com/css2?family=Ubuntu:wght@400;500;700&display=swap">
<style>
  :root {
    --backdrop: #3b3a36;
    --card: #ffffff;
    --ink: #1e1e1e;
    --ink-soft: #333333;
    --accent-blue: #2a8fd0;
    --accent-orange: #f07c1e;
    --accent-green: #7dbb2c;
  }
  * { margin: 0; padding: 0; box-sizing: border-box; }
  html, body {
    width: 1200px;
    height: 869px;
    overflow: hidden;
    background: var(--backdrop);
    font-family: "Ubuntu", sans-serif;
  }
  .canvas {
    position: relative;
    width: 1200px;
    height: 869px;
  }
  .business-card {
    position: absolute;
    left: 180px;
    top: 197px;
    width: 840px;
    height: 475px;
    background: var(--card);
    border-radius: 26px;
  }
  .holder {
    position: absolute;
    left: 79px;
    top: 52px;
    color: var(--ink);
  }
  .holder-name {
    font-size: 34px;
    font-weight: 400;
    line-height: 1.1;
  }
  .holder-title {
    font-size: 20px;
    font-weight: 400;
    margin-top: 6px;
    color: var(--ink-soft);
  }
  .brand {
    position: absolute;
    left: 48px;
    top: 295px;
    display: flex;
    align-items: center;
    gap: 22px;
  }
  .brand-dot {
    width: 120px;
    height: 120px;
    border-radius: 50%;
    background: var(--accent-blue);
  }
  .brand-name {
    font-size: 78px;
    font-weight: 700;
    color: var(--ink);
    letter-spacing: -1px;
  }
  .contact {
    position: absolute;
    left: 595px;
    top: 262px;
    font-size: 20px;
    line-height: 29px;
    color: var(--ink-soft);
  }
  .contact-address { margin-bottom: 4px; }
  .contact-label { margin-right: 6px; }
  .label-phone { color: var(--accent-blue); }
  .label-email { color: var(--accent-orange); }
  .label-web { color: var(--accent-green); }
</style>
</head>
<body>
<main class="canvas">
  <section class="business-card">
    <header class="holder">
      <h1 class="holder-name">Temi Adeyoka</h1>
      <p class="holder-title">President &amp; CEO</p>
    </header>

    <div class="brand">
      <span class="brand-dot"></span>
      <span class="brand-name">Vetrune</span>
    </div>

    <address class="contact" style="font-style: normal;">
      <div class="contact-address">
        4410 Corliss Lane<br>
        Millbrook<br>
        MD 20917
      </div>
      <div><span class="contact-label label-phone">P :</span>555.014.2280</div>
      <div><span class="contact-label label-email">E :</span>temi@vetrune.com</div>
      <div><span class="contact-label label-web">W :</span>www.vetrune.com</div>
    </address>
  </section>
</main>
</body>
</html>
```